Business Card Design Project

for a second hand vintage clothing store. shop name is The Velvet Cupboard

Cards to be double sided

The name on the card is Joanna Whitfield

Information to put on card:

The Velvet Cupboard
Joanna Whitfield (no job title)
42/871 Dunmore St, Glenwick, Harbourton, NSW, 2417.
Mobile: 0412 905 261
Email: thevelvetcupboard@mailbox.com.au
Web: www.thevelvetcupboard.com.au

Target Market(s)

Women looking at vintage clothing

Industry/Entity Type

Clothing

```html
<!DOCTYPE html>
<html lang="en">
<head>
<meta charset="utf-8">
<title>The Velvet Cupboard — Business Card</title>
<link href="https://fonts.googleapis.com/css2?family=Source+Sans+3:wght@400&display=swap" rel="stylesheet">
<style>
  :root {
    --page: #2b2b2d;
    --card: #5a2338;
    --cream: #f3dd9c;
    --amber: #e8901f;
    --rust: #c8472a;
    --brick: #a53a2a;
    --text: #f6ead0;
    --brand: #f3dd9c;
    --shadow: rgba(0, 0, 0, 0.45);
  }
  * { box-sizing: border-box; margin: 0; padding: 0; }
  html, body {
    width: 1200px;
    height: 1200px;
    overflow: hidden;
    background: var(--page);
    font-family: "Source Sans 3", "Myriad Pro", Arial, sans-serif;
  }
  .canvas {
    width: 1200px;
    height: 1200px;
    display: flex;
    flex-direction: column;
    align-items: center;
    justify-content: center;
    gap: 64px;
  }
  .card {
    position: relative;
    width: 800px;
    height: 496px;
    background: var(--card);
    overflow: hidden;
    box-shadow: 0 10px 30px var(--shadow);
  }
  .card-swoosh {
    position: absolute;
    inset: 0;
    width: 100%;
    height: 100%;
  }
  .brand {
    position: absolute;
    display: flex;
    align-items: center;
    gap: 10px;
    color: var(--brand);
    font-weight: 400;
    white-space: nowrap;
    line-height: 1;
  }
  .brand-dot {
    width: 12px;
    height: 12px;
    border-radius: 50%;
    background: var(--amber);
    flex: none;
  }
  .card-front .brand {
    left: 30px;
    top: 196px;
    font-size: 35px;
  }
  .contact {
    position: absolute;
    left: 428px;
    top: 166px;
    list-style: none;
    color: var(--text);
    font-size: 15px;
    line-height: 29px;
    white-space: nowrap;
  }
  .card-back .brand {
    left: 50%;
    top: 218px;
    transform: translateX(-50%);
    font-size: 46px;
  }
</style>
</head>
<body>
<main class="canvas">

  <section class="card card-front" aria-label="Business card front">
    <svg class="card-swoosh" viewBox="0 0 800 496" preserveAspectRatio="none" aria-hidden="true">
      <path fill="var(--cream)" d="M560 0 C690 12 772 90 800 210 L800 160 C772 76 724 26 664 0 Z"/>
      <path fill="var(--brick)" d="M700 0 C752 22 790 64 800 110 L800 0 Z"/>
      <path fill="var(--rust)" d="M800 250 C794 340 772 420 730 496 L800 496 Z"/>
    </svg>
    <div class="brand"><span class="brand-dot"></span>The Velvet Cupboard</div>
    <ul class="contact">
      <li>The Velvet Cupboard</li>
      <li>Joanna Whitfield</li>
      <li>42/871 Dunmore St, Glenwick, Harbourton, NSW, 2417.</li>
      <li>Mobile: 0412 905 261</li>
      <li>Email: thevelvetcupboard@mailbox.com.au</li>
      <li>Web: www.thevelvetcupboard.com.au</li>
    </ul>
  </section>

  <section class="card card-back" aria-label="Business card back">
    <svg class="card-swoosh" viewBox="0 0 800 496" preserveAspectRatio="none" aria-hidden="true">
      <path fill="var(--cream)" d="M0 150 C120 300 420 360 800 280 L800 292 C430 380 140 350 0 210 Z"/>
      <path fill="var(--amber)" d="M0 265 C110 350 300 390 600 380 C400 400 180 400 0 355 Z"/>
    </svg>
    <div class="brand"><span class="brand-dot"></span>The Velvet Cupboard</div>
  </section>

</main>
</body>
</html>
```